Elegant, Playful, Health And Wellness Packaging Design for an Essential Oil Diffuser

Box design for diffuser, should be elegant, luxury, white box with gold foil and vibrant color combination that pops off the white box.

Designs look the same

```html
<!DOCTYPE html>
<html lang="en">
<head>
<meta charset="utf-8">
<title>Aurelle Diffuser Box Dieline</title>
<link href="https://fonts.googleapis.com/css2?family=Arimo&family=Cinzel:wght@400;600&family=Tinos&display=swap" rel="stylesheet">
<style>
  :root {
    --paper: #ffffff;
    --cut-line: #c8432a;
    --gold: #b0851f;
    --gold-light: #e6d5b0;
    --gold-mid: #cdb385;
    --ink: #231815;
    --frame-edge: #a8936a;
  }
  html, body { margin: 0; padding: 0; overflow: hidden; background: var(--paper); }
  .canvas { display: block; width: 1200px; height: 767px; }
  .sheet-border { fill: none; stroke: #999; stroke-width: 2; }
  .dieline { fill: var(--paper); stroke: var(--cut-line); stroke-width: 3; stroke-linejoin: round; }
  .dieline-inner { fill: none; stroke: var(--gold-light); stroke-width: 1; }
  .size-label { font-family: "Arimo", sans-serif; font-size: 82px; fill: var(--ink); letter-spacing: 1px; }
  .brand-name { font-family: "Cinzel", serif; font-weight: 600; fill: var(--gold); text-anchor: middle; letter-spacing: 2px; }
  .brand-mark { fill: none; stroke: var(--gold); stroke-width: 3; }
  .caps-line { font-family: "Cinzel", serif; font-weight: 400; fill: var(--gold); text-anchor: middle; letter-spacing: 1px; }
  .frame-outer { fill: url(#frameGradient); stroke: var(--frame-edge); stroke-width: 1.5; }
  .frame-ornament { fill: url(#ornamentGradient); }
  .frame-field { fill: var(--paper); }
  .copy { font-family: "Tinos", serif; fill: var(--gold); }
  .copy-title { font-size: 8.5px; text-anchor: middle; }
  .copy-body { font-size: 8px; }
  .copy-divider { stroke: var(--gold); stroke-width: 1; }
</style>
</head>
<body>
<svg class="canvas" viewBox="0 0 2408 1540" width="1200" height="767" xmlns="http://www.w3.org/2000/svg">
  <defs>
    <linearGradient id="frameGradient" x1="0" y1="0" x2="1" y2="1">
      <stop offset="0" stop-color="#e9dcbf"/>
      <stop offset="0.5" stop-color="#f3ead6"/>
      <stop offset="1" stop-color="#c9b283"/>
    </linearGradient>
    <linearGradient id="ornamentGradient" x1="0" y1="0" x2="1" y2="0">
      <stop offset="0" stop-color="#8a6a2a"/>
      <stop offset="0.5" stop-color="#c9a45a"/>
      <stop offset="1" stop-color="#8a6a2a"/>
    </linearGradient>
  </defs>

  <rect class="sheet-border" x="1" y="1" width="2406" height="1538"/>

  <text class="size-label" x="1263" y="285">135x135x106mm</text>

  <!-- Box dieline -->
  <path class="dieline" d="
    M326 655 L373 495 Q380 480 400 480 L710 481 Q727 482 727 505 L727 668 L738 688
    L738 258 Q738 230 770 230 L1125 230 Q1152 230 1152 262 L1150 668 L1160 688
    L1160 665 L1160 505 Q1160 480 1190 480 L1497 480 Q1508 484 1515 497 L1563 657 L1563 688
    L1706 688 L1706 655 Q1706 640 1720 640 L1820 640 Q1833 640 1833 655 L1833 688
    L1975 688 L1975 1010 L1872 1218 L1872 1268 Q1872 1278 1862 1278 L1673 1278 Q1663 1278 1663 1268
    L1663 1218 L1563 1012 L1563 1212 Q1563 1220 1555 1220 L1375 1220 Q1355 1220 1355 1200
    L1355 1112 L1150 1013 L1150 1270 Q1150 1278 1142 1278 L1055 1278 Q1047 1278 1047 1270
    L1047 1218 L840 1218 L840 1270 Q840 1278 832 1278 L746 1278 Q738 1278 738 1270
    L738 1015 L532 1115 L532 1195 Q532 1220 508 1220 L333 1220 Q326 1220 326 1213 Z"/>

  <!-- Side panel brand -->
  <g class="side-brand">
    <circle class="brand-mark" cx="534" cy="830" r="22"/>
    <text class="brand-name" x="534" y="875" font-size="22">AURELLE</text>
    <text class="caps-line" x="534" y="892" font-size="10">WWW.AURELLE.COM</text>
  </g>

  <!-- Front label -->
  <g class="front-label">
    <rect class="frame-outer" x="798" y="734" width="292" height="231"/>
    <rect class="frame-ornament" x="808" y="742" width="272" height="215" role="img" aria-label="Gold Greek key border ornament"/>
    <rect class="frame-field" x="815" y="751" width="258" height="199"/>
    <text class="caps-line" x="944" y="769" font-size="10">EXPERIENCE THE ESSENCE OF NATURE</text>
    <circle class="brand-mark" cx="943" cy="828" r="28"/>
    <text class="brand-name" x="943" y="884" font-size="26">AURELLE</text>
    <text class="caps-line" x="944" y="896" font-size="9">Signature Rare Oils Collection</text>
    <text class="caps-line" x="944" y="940" font-size="11">Ultrasonic Diffuser</text>
  </g>

  <!-- Back panel copy -->
  <g class="back-copy copy">
    <text class="copy-title" x="1360" y="746">AURELLE RARE ESSENTIAL OILS DIFFUSER</text>
    <text class="copy-body" x="1196" y="796" textLength="320">Experience the pure essence of nature with the Rare Oils Veda Diffuser. Sourced from the farthest</text>
    <text class="copy-body" x="1196" y="806" textLength="320">reaches of the earth, Aurelle Rare Oils are extracted only from the highest quality and purest raw</text>
    <text class="copy-body" x="1196" y="816" textLength="320">form ingredients. Using the Veda diffuser with Aurelle Rare Oils can help improve health, quality</text>
    <text class="copy-body" x="1196" y="826">of life, and overall spiritual balance.</text>

    <text class="copy-body" x="1199" y="877">Features:</text>
    <text class="copy-body" x="1199" y="898">Continuous diffusing</text>
    <text class="copy-body" x="1199" y="908">Timer settings</text>
    <text class="copy-body" x="1199" y="918">7 LED color &amp; light settings</text>
    <text class="copy-body" x="1199" y="929">Portable</text>
    <text class="copy-body" x="1199" y="939">Pet safe</text>
    <text class="copy-body" x="1199" y="949">Easy to clean</text>

    <line class="copy-divider" x1="1333" y1="875" x2="1333" y2="952"/>

    <text class="copy-body" x="1369" y="898">Dimensions: 135*135*108mm</text>
    <text class="copy-body" x="1369" y="908">Capacity: 300ml</text>
    <text class="copy-body" x="1369" y="918">33 ml/hour output</text>
    <text class="copy-body" x="1369" y="929">Safety Auto-off when empty</text>
    <text class="copy-body" x="1369" y="939">Whisper Quiet</text>
    <text class="copy-body" x="1369" y="949">Contains 1 Veda Diffuser, 1 Power Adaptor</text>
  </g>

  <!-- Opposite side label -->
  <g class="side-label">
    <rect class="frame-outer" x="1617" y="734" width="292" height="231"/>
    <rect class="frame-ornament" x="1626" y="742" width="274" height="215" role="img" aria-label="Gold Greek key border ornament"/>
    <rect class="frame-field" x="1633" y="751" width="260" height="199"/>
    <text class="caps-line" x="1762" y="769" font-size="10">EXPERIENCE THE ESSENCE OF NATURE</text>
    <circle class="brand-mark" cx="1762" cy="822" r="36"/>
    <text class="brand-name" x="1762" y="887" font-size="32">AURELLE</text>
    <text class="caps-line" x="1762" y="912" font-size="12">Signature Rare Oils Collection</text>
  </g>
</svg>
</body>
</html>
```